" Meu nome é Tarcísio Lobato e minha esposa, Celina Fagundes. Somos oftalmologistas e possuímos uma clínica oftalmológica com centro cirúrgico que atende a população da cidade de Pombal e cidades circunvizinhas. Apesar de já estarmos no mercado há mais de 10 anos, com clientela consolidada e de possuírmos uma logomarca, nunca conseguimos emplacar o nome da clínica, que sempre é conhecida como "Clínica da Dra. Celina". Ou seja, este é um "nome" forte que pode ser usado na nova marca. "

```html
<!DOCTYPE html>
<html lang="pt-BR">
<head>
<meta charset="UTF-8">
<title>Cartão de visitas — Clínica da Dra. Celina</title>
<link href="https://fonts.googleapis.com/css2?family=Arimo:wght@400;700&display=swap" rel="stylesheet">
<style>
  :root {
    --page: #cfcfd1;
    --card-white: #ffffff;
    --brand-red: #c8102e;
    --navy: #14406b;
    --navy-deep: #0c2c4f;
    --ink-soft: #6f757d;
    --text-light: #ffffff;
    --text-muted: #b9c8d8;
    --stripe: linear-gradient(90deg, #2a6fb5 0%, #6aa7dd 35%, #c8102e 60%, #f28c1d 80%, #4caf50 100%);
    --stripe-v: linear-gradient(180deg, #2a6fb5 0%, #6aa7dd 35%, #c8102e 60%, #f28c1d 80%, #4caf50 100%);
  }
  * { box-sizing: border-box; margin: 0; padding: 0; }
  html, body { width: 1200px; height: 1200px; overflow: hidden; }
  body {
    background: var(--page);
    font-family: "Arimo", Arial, sans-serif;
    position: relative;
  }
  .card {
    position: absolute;
    top: 456px;
    width: 520px;
    height: 288px;
    overflow: hidden;
  }
  /* Frente */
  .card-front {
    left: 50px;
    background: var(--card-white);
  }
  .brand-name {
    position: absolute;
    left: 0; right: 0;
    top: 96px;
    text-align: center;
    font-size: 36px;
    font-weight: 400;
    color: var(--navy);
    line-height: 1.1;
    white-space: nowrap;
  }
  .brand-tagline {
    position: absolute;
    left: 0; right: 0;
    top: 148px;
    text-align: center;
    font-size: 11px;
    font-weight: 400;
    letter-spacing: 1.5px;
    color: var(--ink-soft);
    text-transform: uppercase;
    white-space: nowrap;
  }
  .front-base {
    position: absolute;
    left: 0; right: 0; bottom: 16px;
    height: 8px;
    background: var(--navy);
  }
  .front-stripe {
    position: absolute;
    left: 0; right: 0; bottom: 24px;
    height: 4px;
    background: var(--stripe);
  }
  /* Verso */
  .card-back {
    left: 630px;
    background: radial-gradient(circle at 30% 45%, #245b8f 0%, var(--navy) 45%, var(--navy-deep) 100%);
  }
  .back-stripe {
    position: absolute;
    top: 0; bottom: 0; right: 0;
    width: 5px;
    background: var(--stripe-v);
  }
  .contact {
    position: absolute;
    left: 280px;
    top: 70px;
    color: var(--text-light);
  }
  .contact-name {
    font-size: 15px;
    font-weight: 700;
    text-transform: uppercase;
    letter-spacing: .3px;
  }
  .contact-role {
    font-size: 9px;
    color: var(--text-muted);
    text-transform: uppercase;
    margin-bottom: 18px;
  }
  .contact-list { list-style: none; }
  .contact-list li {
    display: flex;
    align-items: flex-start;
    gap: 8px;
    font-size: 12px;
    line-height: 1.25;
    margin-bottom: 10px;
    white-space: nowrap;
  }
  .contact-list svg { flex: none; margin-top: 2px; }
</style>
</head>
<body>

  <section class="card card-front" aria-label="Frente do cartão">
    <p class="brand-name">Clínica da Dra. Celina</p>
    <p class="brand-tagline">Oftalmologia e Cirurgia Ocular</p>
    <div class="front-stripe"></div>
    <div class="front-base"></div>
  </section>

  <section class="card card-back" aria-label="Verso do cartão">
    <div class="contact">
      <p class="contact-name">Nome Sobrenome</p>
      <p class="contact-role">Função</p>
      <ul class="contact-list">
        <li>
          <svg width="10" height="10" viewBox="0 0 10 10"><path d="M2 1h2l1 2.5-1.3.8a5 5 0 0 0 2 2L6.5 5 9 6v2a1 1 0 0 1-1 1A7 7 0 0 1 1 2a1 1 0 0 1 1-1z" fill="#c8102e"/></svg>
          <span>(00) 00000.0000 / 00000.0000</span>
        </li>
        <li>
          <svg width="10" height="10" viewBox="0 0 10 10"><rect x="0.5" y="2" width="9" height="6" fill="#c8102e"/><path d="M0.5 2l4.5 3.5L9.5 2" stroke="#14406b" fill="none"/></svg>
          <span>suaempresa@email.com</span>
        </li>
        <li>
          <svg width="10" height="10" viewBox="0 0 10 10"><circle cx="5" cy="5" r="4.2" fill="none" stroke="#c8102e" stroke-width="1.3"/><path d="M1 5h8M5 1v8" stroke="#c8102e"/></svg>
          <span>www.suaempresa.com.br</span>
        </li>
        <li>
          <svg width="10" height="12" viewBox="0 0 10 12"><path d="M5 0a4 4 0 0 1 4 4c0 3-4 8-4 8S1 7 1 4a4 4 0 0 1 4-4z" fill="#c8102e"/><circle cx="5" cy="4" r="1.5" fill="#14406b"/></svg>
          <span>End. completo, 00, Bairro<br>CEP 0000.0000 - Cidade-SP</span>
        </li>
      </ul>
    </div>
    <div class="back-stripe"></div>
  </section>

</body>
</html>
```